Visitenkarten für Mentorin für Frauen
Zielgruppe
Ich bin Mentorin für Frauen (30-50 Jahre alt), die ihre Berufung endlich finden möchten und sich nach mehr Energie und Sinn sehnen. Ich helfe ihnen mit meiner (Name fehtl noch)-Methode ihren Seelenweg zu finden und zu gehen, sodass sie vor Energie übersprudeln und mit einem Leuchten in den Augen ein Leben in Fluss und Fülle kreieren.
Sie sind nicht unglücklich, aber es fehtl ihnen was, das sie wirklich erfüllt.
Stichwörter: Numerologie, Human Design, Seelenweg, Berufung, Lebensaufgabe, erfüllt sein- endlich die Leere füllen, Freiheit, Selbstbestimmt, Selbstliebe, Potentialentfaltung, Transformation
meine core story:
Mit Freude, unglaublicher Energie und einem Strahlen in den Augen schon vor dem Wecker aufzustehen, war für mich früher undenkbar. Ich konnte mir nicht vorstellen, wie sich Leute auf den Montag freuen konnten.
Dabei hätte mich nicht als unglücklich bezeichnet, aber es fehlt einfach etwas, ich hatte eine innere Leere und eine Sehnsucht nach dem Sinn in meinem Lebe, wollte so geliebt werden wie ich bin und mich auch so zeigen können. Ich weiß wie es ist sich klein, unsicher zu fühlen und nicht zu wissen woher das kommt. Ich habe es einfach nicht für möglich gehalten, dass diese innere Leere so leicht zu füllen ist und Freude, Spaß, Selbstbewusstseein und Leichtigkeit in allen Bereichen mit sich bringt.
Weil ich selbst diesen Weg gegangen bin und weil ich weiß, dass es nichts erfüllenderes gibt als das schlummernde Potential zu erwecken, begleite ich Frauen dabei ihren Seelenweg zu finden und zu gehen.
Dadurch dass sie genau wissen, was ihre Gaben sind und was ihre Seele glücklich macht, haben sie Spaß und Freude, gerade auch in den alltäglichen Dingen. Sie führen ein selbstbestimmtes Leben, lieben sich selbst und zeigen sich so wie sie sind.Die gigantische Energie die dadurch in ihnen frei wird, lässt sie die bisherigen Grenzen überwinden. Sie tun was sie erfüllt, o..
Aufgabenstellung
weiblich, geschwungen, weich: beinhalten solls:
Helena Wortmann
Mentorin für Powerfrauen
(Lebe deine Berufung)--> da bin ich mir nicht ganz sicher ob das gut aussehn wird oder zuviel wird
falls relevant habe ich bisher folgende Schriftarten verwendet: Canva Sans und Tan mon cheri
ist aber kein muss

```html
<!DOCTYPE html>
<html lang="de">
<head>
<meta charset="UTF-8">
<title>Helena Wortmann – Visitenkarte</title>
<link rel="stylesheet" href="https://fonts.googleapis.com/css2?family=Pinyon+Script&family=Nunito+Sans:wght@500;600&display=swap">
<style>
  :root {
    --paper: #fdf5eb;
    --gold: #b8862e;
    --brown: #55381a;
    --ink: #4a3212;
    --art-a: #f7e8d4;
    --art-b: #eed7b6;
  }
  html, body {
    margin: 0;
    padding: 0;
    overflow: hidden;
    background: var(--paper);
  }
  .card {
    position: relative;
    width: 1200px;
    height: 686px;
    background: var(--paper);
    overflow: hidden;
  }
  .arch-frame {
    position: absolute;
    inset: 0;
  }
  .name {
    position: absolute;
    left: 262px;
    top: 146px;
    margin: 0;
    font-family: "Pinyon Script", cursive;
    font-weight: 400;
    font-size: 66px;
    line-height: 1;
    color: var(--brown);
    white-space: nowrap;
    -webkit-text-stroke: 0.6px var(--brown);
  }
  .tagline {
    position: absolute;
    left: 264px;
    top: 238px;
    margin: 0;
    font-family: "Pinyon Script", cursive;
    font-size: 44px;
    line-height: 1;
    color: var(--gold);
    white-space: nowrap;
  }
  .contact-list {
    position: absolute;
    left: 277px;
    top: 337px;
    margin: 0;
    padding: 0;
    list-style: none;
  }
  .contact-item {
    display: flex;
    align-items: center;
    height: 50px;
    font-family: "Nunito Sans", sans-serif;
    font-weight: 600;
    font-size: 30px;
    color: var(--ink);
    white-space: nowrap;
  }
  .contact-icon {
    width: 40px;
    height: 40px;
    margin-right: 32px;
    flex: none;
  }
  .portrait-art {
    position: absolute;
    left: 778px;
    top: 137px;
    width: 332px;
    height: 410px;
    border-radius: 160px 160px 24px 24px;
    background: radial-gradient(ellipse at 55% 40%, var(--art-a), var(--art-b));
  }
</style>
</head>
<body>
<main class="card">
  <svg class="arch-frame" width="1200" height="686" viewBox="0 0 1200 686" aria-hidden="true">
    <g fill="none" stroke="var(--gold)" stroke-width="2">
      <path d="M903 69 H361 A272.5 272.5 0 0 0 361 614 H903"/>
      <path d="M903 90 H361 A251 251 0 0 0 361 592 H903"/>
    </g>
  </svg>

  <h1 class="name">Helena Wortmann</h1>
  <p class="tagline">Mentorin für Powerfrauen</p>

  <ul class="contact-list">
    <li class="contact-item">
      <svg class="contact-icon" viewBox="0 0 40 40" aria-hidden="true">
        <circle cx="20" cy="20" r="18" fill="none" stroke="var(--gold)" stroke-width="2"/>
        <path d="M14 11 l4 0 l1.5 5 l-2.5 2 a12 12 0 0 0 5 5 l2 -2.5 l5 1.5 l0 4 a2 2 0 0 1 -2 2 a17 17 0 0 1 -15 -15 a2 2 0 0 1 2 -2z" fill="none" stroke="var(--gold)" stroke-width="1.8" stroke-linejoin="round"/>
      </svg>
      +49 170 5550182
    </li>
    <li class="contact-item">
      <svg class="contact-icon" viewBox="0 0 40 40" aria-hidden="true">
        <circle cx="20" cy="20" r="18" fill="none" stroke="var(--gold)" stroke-width="2"/>
        <rect x="10" y="13" width="20" height="14" rx="1" fill="none" stroke="var(--gold)" stroke-width="1.8"/>
        <path d="M10 13 L20 21 L30 13 M10 27 L17 19 M30 27 L23 19" fill="none" stroke="var(--gold)" stroke-width="1.5"/>
      </svg>
      hallo@helenawortm.de
    </li>
    <li class="contact-item">
      <svg class="contact-icon" viewBox="0 0 40 40" aria-hidden="true">
        <circle cx="20" cy="20" r="18" fill="none" stroke="var(--gold)" stroke-width="2"/>
        <circle cx="20" cy="20" r="10" fill="none" stroke="var(--gold)" stroke-width="1.6"/>
        <ellipse cx="20" cy="20" rx="4.5" ry="10" fill="none" stroke="var(--gold)" stroke-width="1.4"/>
        <path d="M10 20 H30 M12 15 H28 M12 25 H28" stroke="var(--gold)" stroke-width="1.3"/>
      </svg>
      www.helenawortm.de
    </li>
    <li class="contact-item">
      <svg class="contact-icon" viewBox="0 0 40 40" aria-hidden="true">
        <circle cx="20" cy="20" r="18" fill="none" stroke="var(--gold)" stroke-width="2"/>
        <path d="M20 30 C14 23 13 20 13 17.5 a7 7 0 0 1 14 0 C27 20 26 23 20 30z" fill="var(--gold)"/>
        <circle cx="20" cy="17.5" r="2.6" fill="var(--paper)"/>
      </svg>
      Lindenweg 12, Sonnenstadt
    </li>
  </ul>

  <div class="portrait-art" role="img" aria-label="Feine Linienzeichnung einer Frau mit langem Haar und Schmetterling, umgeben von goldenen Funkelsternen"></div>
</main>
</body>
</html>
```